Bulk Food Container sticker

Our company sells bulk snacks to office locations. We re-package all sorts of foods into re-usable "Stowvessel" type containers for consistency. We need to create a designed sticker which has room to laser-print the name of the food. The "blank" sticker needs to be designed with our logo, etc... I have attached 2 files. The first is an example from another company doing a similar work, and the second is the template from the company that will be printing the stickers for me. See our website for examples of our current corporate identity. www.brindlemarsh.example
Target Market(s)
Offices, tech companies
Industry/Entity Type
Printing
Look and feel
Each slider illustrates characteristics of the customer's brand and the style your logo design should communicate.

```html
<!DOCTYPE html>
<html lang="en">
<head>
<meta charset="utf-8">
<title>Brindlemarsh container sticker – tagline options</title>
<link rel="stylesheet" href="https://fonts.googleapis.com/css2?family=Arimo:wght@400;700&display=swap">
<style>
  :root {
    --brown: #7f4a00;
    --orange: #df6d04;
    --white: #ffffff;
    --page: #ffffff;
  }
  html, body {
    margin: 0;
    padding: 0;
    width: 1200px;
    height: 1146px;
    overflow: hidden;
    background: var(--page);
  }
  .sheet {
    position: relative;
    width: 1200px;
    height: 1146px;
  }
  .sticker {
    position: absolute;
    width: 450px;
    height: 452px;
    display: block;
    font-family: "Arimo", Arial, sans-serif;
  }
  .sticker--caps { left: 105px; top: 69px; }
  .sticker--lower { left: 651px; top: 69px; }
  .sticker--sentence { left: 106px; top: 618px; }

  .sticker__base { fill: var(--brown); }
  .sticker__accent { fill: var(--orange); }
  .sticker__label { fill: var(--white); }
  .brand-name {
    fill: var(--white);
    font-weight: 700;
    font-size: 37px;
  }
  .brand-service {
    fill: var(--white);
    font-weight: 400;
    font-size: 11.5px;
    letter-spacing: 3px;
  }
  .tagline {
    fill: var(--brown);
    font-weight: 700;
    font-size: 16.5px;
  }
  .tagline__sub {
    fill: var(--orange);
    font-weight: 700;
    font-size: 11px;
  }
  .web-address {
    fill: var(--white);
    font-weight: 700;
    font-size: 17.5px;
  }
</style>
</head>
<body>
<main class="sheet">

  <svg class="sticker sticker--caps" viewBox="0 0 394 396" aria-label="Sticker with uppercase tagline">
    <defs>
      <clipPath id="sticker-shape-a"><rect width="394" height="396" rx="10"/></clipPath>
    </defs>
    <g clip-path="url(#sticker-shape-a)">
      <rect class="sticker__base" width="394" height="396"/>
      <polygon class="sticker__accent" points="394,55 394,396 0,396 0,332 200,318 330,150"/>
    </g>
    <rect class="sticker__label" x="26" y="102" width="344" height="248" rx="18"/>
    <text class="brand-name" x="197" y="71" text-anchor="middle">Brindlemarsh</text>
    <text class="brand-service" x="320" y="92" text-anchor="end">COFFEE SERVICE</text>
    <text class="tagline" x="48" y="301">ENHANCING OFFICE</text>
    <text class="tagline" x="48" y="323">PRODUCTIVITY...</text>
    <text class="tagline__sub" x="48" y="337">ONE TUB AT A TIME</text>
    <text class="web-address" x="197" y="377" text-anchor="middle">www.brindlemarsh.example</text>
  </svg>

  <svg class="sticker sticker--lower" viewBox="0 0 394 396" aria-label="Sticker with lowercase tagline">
    <defs>
      <clipPath id="sticker-shape-b"><rect width="394" height="396" rx="10"/></clipPath>
    </defs>
    <g clip-path="url(#sticker-shape-b)">
      <rect class="sticker__base" width="394" height="396"/>
      <polygon class="sticker__accent" points="394,55 394,396 0,396 0,332 200,318 330,150"/>
    </g>
    <rect class="sticker__label" x="26" y="102" width="344" height="248" rx="18"/>
    <text class="brand-name" x="197" y="71" text-anchor="middle">Brindlemarsh</text>
    <text class="brand-service" x="320" y="92" text-anchor="end">COFFEE SERVICE</text>
    <text class="tagline" x="48" y="302">enhancing office</text>
    <text class="tagline" x="48" y="324">productivity...</text>
    <text class="tagline__sub" x="48" y="338">one tub at a time</text>
    <text class="web-address" x="197" y="377" text-anchor="middle">www.brindlemarsh.example</text>
  </svg>

  <svg class="sticker sticker--sentence" viewBox="0 0 394 396" aria-label="Sticker with sentence-case tagline">
    <defs>
      <clipPath id="sticker-shape-c"><rect width="394" height="396" rx="10"/></clipPath>
    </defs>
    <g clip-path="url(#sticker-shape-c)">
      <rect class="sticker__base" width="394" height="396"/>
      <polygon class="sticker__accent" points="394,55 394,396 0,396 0,332 200,318 330,150"/>
    </g>
    <rect class="sticker__label" x="26" y="102" width="344" height="248" rx="18"/>
    <text class="brand-name" x="197" y="71" text-anchor="middle">Brindlemarsh</text>
    <text class="brand-service" x="320" y="92" text-anchor="end">COFFEE SERVICE</text>
    <text class="tagline" x="48" y="302">Enhancing office</text>
    <text class="tagline" x="48" y="324">productivity...</text>
    <text class="tagline__sub" x="48" y="338">one tub at a time</text>
    <text class="web-address" x="197" y="377" text-anchor="middle">www.brindlemarsh.example</text>
  </svg>

</main>
</body>
</html>
```